House Cleaning Website - Maid Services

Logo, landing page design with contact form - coded MUST BE MOBILE FRIENDLY

Cleaning business - maid service - i've added a few example websites

Clean, Smart Website Design that is built for getting leads

CONTENT FOR HOME PAGE -

Cleaning Seminole County Homes For Over 12 Years

Rosetta Cleans

* Trusted by your neighbors for more than a decade
* Affordable and flexible to accommodate your needs
* 200% Money Back Guarantee
* Up to 20% Discount on Continued Cleanings
* Same Day Cleanings

My Clients Are Happy
"Rosetta has been cleaning my home for the past 3 1/2 years and I couldn't be happier with her. I trust her with cleaning my home while I'm out of town and recommend her to my friends."

Target Market(s)

people looking for house cleaning

Industry/Entity Type

Cleaning Service

Contact Information for Business Card

Rosetta Cleans -
#321-555-0187
200% Guarantee
on back of card - $25 Referral Fee

Logo Text

Rosetta Cleans

Coding

Coded - Design and coding required

Number of Pages Required

3 page

Requirements
Must have
• 4 links in top toolbar - services, contact, free estimate and about
• *contact will be a popup form to contact
• *services will be a graphic similar to the one on this page ... https://www.brightbroomcrew.com/maid-services/
• *free estimate link will be a page with same questions as
• Must have landing page concept - I will be advertising to get people to submit their information...
• 1. Must have a "Request FREE Estimate" button that pops up a box for them to submit their information - name, number, email. Once they submit this information, they will be taken to a 2nd form to complete their details - If they dont complete the 2nd part I still receive the 1st part to call. The 2nd part will have same questions ashttps://www.tidyhenwick.com/local-house-cleaning/fl/west-miami/request-a-cleaning.aspx?cpgnId=FE0CA3B4-3A4C-4D9C-9B11-E69492B42092&scid=3554195&cid=2303288&tc=17072613580054989&rl_key=a0563857ec931d2a952e39d66a08939d&kw=77903:7716&pub_cr_id=200261568213&dynamic_proxy=1&primary_serv=www.tidyhenwick.com&rl_track_landing_pages=1
• 2. Must have pricing like https://www.brightbroomcrew.com/ 1 bedroom through 6 bedroom pricing base pricing graphic.
• 2.Must have a 200% satisfaction guarantee graphic
• 3.Must have phone number visible
• 4. graphics offering - 1st deep clean $25 Off - 10% Off Bi Weekly Cleanings - 20% Off Weekly Cleanings
• I like the clean look of this website https://www.pearlofsuds.com/ BUT want a more compact website like https://www.brightbroomcrew.com/
• Popup for when the try and x out saying Book Now And Receive $20 Off 1st Cleaning

```html
<!DOCTYPE html>
<html lang="en">
<head>
<meta charset="utf-8">
<title>Rosetta Cleans – Maid Services</title>
<link rel="stylesheet" href="https://fonts.googleapis.com/css2?family=Roboto:wght@300;400;500;700&display=swap">
<style>
  :root {
    --teal: #47d5c5;
    --teal-dark: #2fa89a;
    --teal-deep: #23887d;
    --coral: #f97d7b;
    --ink: #1f1f1f;
    --field: #f1f5f6;
    --rule: #d6d6d6;
    --white: #ffffff;
  }
  * { box-sizing: border-box; margin: 0; padding: 0; }
  html, body { width: 1200px; height: 775px; overflow: hidden; background: var(--white); }
  body { font-family: "Roboto", Arial, sans-serif; color: var(--ink); position: relative; }

  .site-header { position: absolute; left: 0; top: 0; width: 1200px; height: 71px; border-bottom: 1px solid var(--rule); }
  .brand { position: absolute; left: 98px; top: 12px; font-size: 40px; font-weight: 500; color: var(--teal); letter-spacing: 0.5px; }
  .header-phone { position: absolute; left: 962px; top: 5px; display: flex; align-items: center; gap: 6px; }
  .header-phone .label { font-size: 11px; color: var(--teal); line-height: 12px; }
  .header-phone .number { font-size: 14px; color: #333; line-height: 16px; font-weight: 300; }
  .main-nav { position: absolute; right: 100px; top: 41px; display: flex; gap: 23px; align-items: center; }
  .main-nav a { font-size: 14px; font-weight: 500; color: var(--ink); text-decoration: none; }
  .main-nav a.is-active { color: var(--teal); border: 1px solid var(--teal); border-radius: 12px; padding: 2px 11px; margin-right: -10px; }

  .hero-illustration { position: absolute; left: 90px; top: 94px; width: 433px; height: 456px;
    background: radial-gradient(ellipse at 50% 92%, #eeeeee 0 38%, transparent 39%),
                linear-gradient(180deg, #ffffff 0%, #f7f2f7 60%, #ffffff 100%); border-radius: 8px; }

  .promo-disc { position: absolute; left: 503px; top: 224px; width: 278px; height: 278px; border-radius: 50%; background: var(--teal); overflow: hidden; }
  .promo-disc .title { position: absolute; left: 87px; top: 37px; color: var(--white); font-size: 33px; font-weight: 500; line-height: 29px; }
  .promo-disc .divider { position: absolute; left: 87px; top: 99px; width: 190px; height: 1px; background: rgba(255,255,255,0.8); }
  .promo-disc .call { position: absolute; left: 87px; top: 104px; font-size: 16px; font-weight: 500; color: var(--ink); }
  .promo-disc .phone { position: absolute; left: 87px; top: 123px; font-size: 20px; font-weight: 300; color: var(--ink); }
  .supplies-art { position: absolute; left: 520px; top: 383px; width: 219px; height: 120px;
    background: linear-gradient(90deg, #f6a04b 0%, #e9473f 40%, #f5c84a 70%, #2b7fd3 100%); border-radius: 6px; opacity: 0.85; }

  .estimate-card { position: absolute; left: 797px; top: 154px; width: 312px; height: 387px; background: var(--teal); border-radius: 3px; overflow: hidden; }
  .estimate-card .cap { position: absolute; left: 0; top: 0; }
  .estimate-card h2 { position: absolute; top: 19px; width: 100%; text-align: center; color: var(--white); font-size: 29px; font-weight: 500; }
  .estimate-card .intro { position: absolute; top: 99px; left: 20px; right: 20px; text-align: center; color: var(--white); font-size: 12px; font-weight: 300; line-height: 18px; }
  .field { position: absolute; left: 30px; width: 252px; height: 30px; background: var(--field); border-radius: 2px; font-size: 12px; color: #888; padding: 8px 12px; font-weight: 300; }
  .field.select svg { position: absolute; right: 10px; top: 12px; }
  .submit-btn { position: absolute; left: 62px; top: 320px; width: 192px; height: 44px; background: var(--coral); color: var(--white); font-size: 19px; font-weight: 500; display: flex; align-items: center; justify-content: center; border-radius: 2px; }

  .offers-band { position: absolute; left: 0; top: 578px; width: 1200px; height: 197px; }
  .offer { position: absolute; top: 629px; display: flex; align-items: center; gap: 8px; }
  .badge { width: 118px; height: 118px; border-radius: 50%; background: radial-gradient(circle at 40% 35%, #4cbdb0, var(--teal-deep)); box-shadow: 0 0 0 3px rgba(255,255,255,0.12); display: flex; flex-direction: column; align-items: center; justify-content: center; color: var(--white); position: relative; }
  .badge::after { content: ""; position: absolute; inset: 8px; border: 1px dashed rgba(255,255,255,0.85); border-radius: 50%; }
  .badge .top { font-size: 17px; font-weight: 500; line-height: 16px; text-align: center; }
  .badge .amount { font-size: 27px; font-weight: 500; margin-top: 2px; }
  .badge .amount small { font-size: 12px; }
  .offer .caption { color: var(--white); font-size: 16px; font-weight: 500; }
  .offer-divider { position: absolute; top: 636px; width: 1px; height: 104px; background: rgba(255,255,255,0.7); }
</style>
</head>
<body>
  <header class="site-header">
    <div class="brand">Rosetta Cleans</div>
    <div class="header-phone">
      <svg width="26" height="26" viewBox="0 0 26 26" aria-hidden="true">
        <circle cx="13" cy="13" r="13" fill="var(--teal)"/>
        <path d="M9 7c1 0 2 2.5 2 3s-1 1-1 1.5 2 3.5 4 4.5c.5 0 1-1 1.5-1s3 1 3 2-1.5 2-2.5 2C11 19 7 14 7 9c0-1 1-2 2-2z" fill="#fff"/>
      </svg>
      <div><div class="label">Call us today</div><div class="number">0800 555 010 247</div></div>
    </div>
    <nav class="main-nav">
      <a href="#" class="is-active">Home</a>
      <a href="#">Services</a>
      <a href="#">Contact</a>
      <a href="#">Free Estimate</a>
      <a href="#">About</a>
    </nav>
  </header>

  <div class="hero-illustration" role="img" aria-label="Illustration of a housekeeper vacuuming with a duster in hand"></div>

  <div class="promo-disc">
    <div class="title">Maid<br>Services</div>
    <div class="divider"></div>
    <div class="call">Call us today</div>
    <div class="phone">0800 555 010 247</div>
  </div>
  <div class="supplies-art" role="img" aria-label="Illustration of cleaning supplies: mop, bucket with gloves, bottles and dustpan"></div>

  <section class="estimate-card">
    <svg class="cap" width="312" height="84" viewBox="0 0 312 84" aria-hidden="true">
      <path d="M0 30 Q156 112 312 30 L312 40 Q156 118 0 40 Z" fill="var(--teal-dark)" opacity="0.6"/>
      <path d="M0 0 H312 V30 Q156 112 0 30 Z" fill="var(--coral)"/>
    </svg>
    <h2>Free Estimate</h2>
    <p class="intro">Lorem Ipsum is simply dummy text of the printing and typesetting industry</p>
    <div class="field" style="top:151px">Name</div>
    <div class="field" style="top:193px">Email</div>
    <div class="field" style="top:233px">Phone</div>
    <div class="field select" style="top:274px">Service
      <svg width="11" height="7" viewBox="0 0 11 7" aria-hidden="true"><path d="M1 1l4.5 4.5L10 1" stroke="var(--coral)" stroke-width="1.6" fill="none"/></svg>
    </div>
    <div class="submit-btn">Submit</div>
  </section>

  <svg class="offers-band" width="1200" height="197" viewBox="0 0 1200 197" aria-hidden="true">
    <defs>
      <pattern id="scallop" width="20" height="14" patternUnits="userSpaceOnUse">
        <circle cx="10" cy="14" r="10" fill="var(--teal)"/>
      </pattern>
    </defs>
    <rect x="0" y="0" width="1200" height="14" fill="url(#scallop)"/>
    <rect x="0" y="13" width="1200" height="184" fill="var(--teal)"/>
  </svg>

  <div class="offer" style="left:91px">
    <div class="badge"><div class="top">1st Time</div><div class="amount">$25<small>Off</small></div></div>
    <div class="caption">1st deep clean $25 Off</div>
  </div>
  <div class="offer-divider" style="left:406px"></div>
  <div class="offer" style="left:425px">
    <div class="badge"><div class="top">Weekly<br>Cleanings</div><div class="amount">10%<small>Off</small></div></div>
    <div class="caption">10% Off Bi Weekly Cleanings</div>
  </div>
  <div class="offer-divider" style="left:777px"></div>
  <div class="offer" style="left:790px">
    <div class="badge"><div class="top">Weekly<br>Cleanings</div><div class="amount">20%<small>Off</small></div></div>
    <div class="caption">20% Off Weekly Cleanings</div>
  </div>
</body>
</html>
```